Harbor Lane Coaching

We would like to refresh the design of our current website. We want to make it cleaner, more open and more professional looking using simple page layouts and crisp fonts. The site should be lighter and be easy to navigate.

It is important that it be easy to add and change content.

The current site can be seen at www.harborlanecoach.example

As part of this, we want our logo colors to be darker blue and green more professional than they are currently. The current logo is attached as you can see the colors are too "neon"

THIS IS A WEBSITE DESIGN REFRESH PROJECT

Target Market(s)

Executives

Industry/Entity Type

Cleaner

Font styles to use
Sans Serif

Colors
0355a3
cfdfed
9bcb3c

Requirements
Must have
• Ease of use, ease of adding content
Should not have
• No crazy colors, not too busy...

```html
<!DOCTYPE html>
<html lang="en">
<head>
<meta charset="utf-8">
<title>Harbor Lane Coaching</title>
<link href="https://fonts.googleapis.com/css2?family=Open+Sans:wght@300;400;600&family=Arimo:wght@400;700&display=swap" rel="stylesheet">
<style>
:root{
  --blue:#0355a3;
  --link-blue:#2f6cc0;
  --button-blue:#3168c2;
  --green:#9bcb3c;
  --pale:#cfdfed;
  --text:#555;
  --rule:#ddd;
  --footer:#474747;
  --footer-text:#e6e6e6;
}
*{margin:0;padding:0;box-sizing:border-box}
html,body{width:914px;height:1200px;overflow:hidden;background:#fff}
body{position:relative;font-family:"Arimo",Arial,sans-serif;color:var(--text)}
.abs{position:absolute}
.heading{font-family:"Open Sans",Arial,sans-serif;font-weight:300;color:var(--link-blue)}

/* header */
.brand{left:130px;top:22px;display:flex;align-items:center;gap:8px}
.brand-mark{width:26px;height:26px;border-radius:50%;background:var(--blue)}
.brand-name{font-family:"Open Sans",sans-serif;font-weight:600;font-size:19px;color:var(--blue);line-height:1}
.brand-tag{left:131px;top:64px;font-size:5px;letter-spacing:.3px;text-transform:uppercase;color:var(--blue)}
.follow{right:130px;top:37px;display:flex;align-items:center;gap:6px;font-size:9px;color:#666}
.follow span.dot{width:21px;height:21px;border-radius:50%;background:#c4c4c4;display:block}

/* nav */
.nav{left:0;top:80px;width:914px;height:30px;background:var(--blue)}
.nav ul{list-style:none;position:absolute;left:131px;top:0;display:flex;height:30px}
.nav li{height:30px;line-height:30px;font-size:8px;color:#fff;text-transform:uppercase;text-align:center}
.nav li.active{background:var(--green)}

/* hero */
.hero{left:130px;top:124px;width:653px;height:242px;background:linear-gradient(110deg,#b9c8d3 0%,#8c8c88 35%,#c8b7a4 60%,#7a6656 100%)}
.hero-shadow{left:100px;top:362px;width:714px;height:16px;background:radial-gradient(ellipse at top,rgba(0,0,0,.18),rgba(0,0,0,0) 70%)}
.caption{left:130px;height:30px;line-height:30px;padding:0 13px;background:rgba(60,60,60,.82);color:#fff;font-family:"Open Sans",sans-serif;font-weight:600;font-size:12px;text-transform:uppercase}
.hero-arrows{left:734px;top:339px;display:flex;gap:1px}
.hero-arrows span{width:17px;height:17px;background:rgba(255,255,255,.25);color:#fff;font-size:10px;line-height:17px;text-align:center}
.hero-fade{left:130px;top:366px;width:653px;height:40px;background:linear-gradient(#eee,#fff)}

/* features */
.feature{top:410px;width:200px}
.feature .icon{position:absolute;left:0;top:0;width:32px;height:32px;background:var(--button-blue)}
.feature h3{position:absolute;left:44px;top:1px;font-size:11.5px;white-space:nowrap}
.feature p{position:absolute;left:44px;top:21px;width:150px;font-size:7.4px;line-height:15px}
.divider{left:130px;top:494px;width:653px;height:1px;background:var(--rule)}

/* welcome */
.welcome-title{left:0;top:517px;width:914px;text-align:center;font-size:15px}
.welcome-text{left:140px;top:550px;width:634px;text-align:center;font-size:8px;line-height:16px}

/* cards */
.card-photo{top:609px;width:201px;height:106px}
.card-title{top:725px;font-size:15px}
.card-text{top:750px;width:205px;font-size:7.4px;line-height:15.7px}
.btn{height:25px;width:78px;line-height:25px;background:var(--button-blue);color:#fff;font-size:8px;text-align:center;text-transform:uppercase}
.testi-arrows{left:764px;top:608px;font-size:10px;color:#999;letter-spacing:4px}
.testi-name{left:583px;top:636px;font-size:7.6px;color:#333}
.testi-name em{color:#666}
.testi-name b{color:var(--blue);font-weight:400}
.testi-photo{left:583px;top:660px;width:81px;height:84px;background:linear-gradient(#8a7765,#4b4b52)}
.testi-side{left:679px;top:655px;width:106px;font-size:7.4px;line-height:15.8px}
.testi-rest{left:583px;top:753px;width:200px;font-size:7.4px;line-height:15.8px}

/* about */
.about-title{left:130px;top:886px;font-size:21px}
.about-text{left:130px;top:924px;width:390px;font-size:7.4px;line-height:16.9px}
.about-photo{left:552px;top:893px;width:231px;height:168px;background:linear-gradient(150deg,#e8eef2,#b7c4cc 55%,#6e84a5)}

/* footer */
.footer{left:0;top:1103px;width:914px;height:97px;background:var(--footer);color:var(--footer-text);font-size:7.6px}
.footer-nav{position:absolute;left:132px;top:35px;display:flex;gap:0}
.footer-nav span{margin-right:28px}
.copy{position:absolute;left:132px;top:57px}
.contact{position:absolute;left:619px;top:17px;line-height:15.6px}
.contact .row{display:flex;align-items:flex-start;gap:9px}
.contact svg{margin-top:3px;flex:none}
</style>
</head>
<body>

<header>
  <div class="abs brand"><span class="brand-mark"></span><span class="brand-name">Harbor Lane Coaching</span></div>
  <div class="abs brand-tag">Coaching leaders and companies from distress to success</div>
  <div class="abs follow">Follow Us :<span class="dot"></span><span class="dot"></span><span class="dot"></span></div>
</header>

<nav class="abs nav">
  <ul>
    <li class="active" style="width:72px">Home</li>
    <li style="width:103px">Why Coaching</li>
    <li style="width:42px">About</li>
    <li style="width:95px">Services</li>
    <li style="width:64px">Clients</li>
    <li style="width:102px">Resources</li>
    <li style="width:70px">Contact</li>
    <li style="width:79px">More</li>
  </ul>
</nav>

<section>
  <div class="abs hero" role="img" aria-label="Photo of an executive in conversation with two colleagues at a meeting"></div>
  <div class="abs caption" style="top:279px">Harbor Lane Coaching</div>
  <div class="abs caption" style="top:315px">Works with executives and companies</div>
  <div class="abs hero-arrows"><span>&#8249;</span><span>&#8250;</span></div>
  <div class="abs hero-shadow"></div>
</section>

<section>
  <div class="abs feature" style="left:143px">
    <div class="icon"><svg width="32" height="32" viewBox="0 0 32 32"><circle cx="16" cy="12" r="4.5" fill="#fff"/><path d="M8 24c0-5 3.5-7 8-7s8 2 8 7z" fill="#fff"/></svg></div>
    <h3 class="heading">Leadership Coaching</h3>
    <p>The Stream of Consciousness, flows through only a few of the world's best organizations...</p>
  </div>
  <div class="abs feature" style="left:351px">
    <div class="icon"><svg width="32" height="32" viewBox="0 0 32 32"><rect x="9" y="8" width="14" height="16" fill="none" stroke="#fff" stroke-width="1.6"/><path d="M12 13h8M12 16.5h8M12 20h5" stroke="#fff" stroke-width="1.4"/></svg></div>
    <h3 class="heading">Assessments</h3>
    <p>The Stream of Consciousness, flows through only a few of the world's best organizations...</p>
  </div>
  <div class="abs feature" style="left:580px">
    <div class="icon"><svg width="32" height="32" viewBox="0 0 32 32"><rect x="8" y="15" width="4" height="9" fill="#fff"/><path d="M13 15l4-7c1.5 0 2 1 1.8 2.5L18 14h5c1.2 0 2 1 1.7 2.2l-1.6 6.5c-.3 1-1 1.3-2 1.3H13z" fill="#fff"/></svg></div>
    <h3 class="heading">Skills Coaching</h3>
    <p>The Stream of Consciousness, flows through only a few of the world's best organizations...</p>
  </div>
  <div class="abs divider"></div>
</section>

<section>
  <h2 class="abs heading welcome-title">Welcome to Harbor Lane Coaching</h2>
  <p class="abs welcome-text">Harbor Lane Coaching works with executives and companies that are facing issues ranging from &nbsp;mild dysfunction to significant distress. We help them pivot, regain control and achieve renewed growth. Harbor Lane Coaching employs the Clear Path Leadership process developed by Elaine M. Carter PhD.</p>
</section>

<section>
  <div class="abs card-photo" style="left:129px;background:linear-gradient(135deg,#5f88ad,#8fb3cf 60%,#36556f)" role="img" aria-label="Chalkboard with coaching related words being written by hand"></div>
  <h3 class="abs heading card-title" style="left:130px">Why Coaching</h3>
  <p class="abs card-text" style="left:130px">Coaching Helps Inspire Individuals Towards Positive and Sustainable Action. Harbor Lane Coaching brings significant business leadership...</p>
  <div class="abs btn" style="left:130px;top:811px">Read More</div>

  <div class="abs card-photo" style="left:352px;background:linear-gradient(135deg,#d9d6d2,#b5846a 50%,#6c6c70)" role="img" aria-label="Team members stacking their hands together"></div>
  <h3 class="abs heading card-title" style="left:353px">Resources</h3>
  <p class="abs card-text" style="left:353px">Coaching Helps Inspire Individuals Towards Positive and Sustainable Action. Harbor Lane Coaching brings significant business leadership...</p>
  <div class="abs btn" style="left:353px;top:811px">Read More</div>

  <h3 class="abs heading card-title" style="left:581px;top:602px">Testimonials</h3>
  <div class="abs testi-arrows">&#8249; &#8250;</div>
  <p class="abs testi-name"><b>Marcus T.</b>,, <em>COO of a Global Event Management</em></p>
  <div class="abs testi-photo" role="img" aria-label="Portrait photo of the client giving the testimonial"></div>
  <p class="abs testi-side">'ve known Daniel Reyes, through business, for a number of years. I became a client of Harbor Lane Coaching at the beginning of 2012 and it's easily one of the best</p>
  <p class="abs testi-rest">decisions I made this year. Daniel is my "go to" advisor and he has been invaluable to me both professionally and personally. I love that he operates...</p>
  <div class="abs btn" style="left:583px;top:811px">Read More</div>
</section>

<section>
  <h2 class="abs heading about-title">About Harbor Lane Coaching</h2>
  <p class="abs about-text">Harbor Lane Coaching works with executives and companies that are facing issues ranging from &nbsp;mild dysfunction to significant distress. We help them pivot, regain control and achieve renewed growth. Harbor Lane Coaching employs the Clear Path Leadership process developed by Elaine M. Carter PhD., founder of the Northfield Institute for Coaching Studies (NICS). Clear Path Leadership is the process that develops a personally effective style of leadership that positively influences and changes not only the leader, but also those with whom they work and interact, as well as their organization as a whole.</p>
  <div class="abs btn" style="left:130px;top:1038px">Read More</div>
  <div class="abs about-photo" role="img" aria-label="Business team gathered around a meeting table with a laptop"></div>
</section>

<footer class="abs footer">
  <div class="footer-nav"><span>Home</span><span>Why Coaching</span><span>About</span><span>Services</span><span>Clients</span><span>Resources</span><span>Contact</span><span>More</span></div>
  <div class="copy">© 2014 Harbor Lane Coaching. All rights reserved.</div>
  <div class="contact">
    <div class="row"><svg width="7" height="9" viewBox="0 0 7 9"><path d="M3.5 0A3.3 3.3 0 0 0 .2 3.3C.2 5.8 3.5 9 3.5 9s3.3-3.2 3.3-5.7A3.3 3.3 0 0 0 3.5 0z" fill="#aaa"/><circle cx="3.5" cy="3.3" r="1.2" fill="#474747"/></svg><div>218 Meadowbrook Road, Suite 4-B<br>Fairview, VA 20100</div></div>
    <div class="row" style="margin-top:4px"><svg width="7" height="10" viewBox="0 0 7 10"><rect x=".5" y=".5" width="6" height="9" rx="1" fill="none" stroke="#aaa"/></svg><div>(555) 010-2843, &nbsp;&nbsp;<svg width="9" height="8" viewBox="0 0 9 8" style="margin:0 3px -1px 0"><rect x="2" y="0" width="5" height="3" fill="#aaa"/><rect x="0" y="3" width="9" height="4" fill="#aaa"/></svg> (555) 010-7719</div></div>
    <div class="row" style="margin-top:4px"><svg width="10" height="8" viewBox="0 0 10 8"><rect x=".5" y=".5" width="9" height="7" fill="none" stroke="#aaa"/><path d="M.5 .5l4.5 4 4.5-4" fill="none" stroke="#aaa"/></svg><div>info@harborlanecoach.example</div></div>
  </div>
</footer>

</body>
</html>
```